Flyer for Belcrest Family Dental

we need a flyer to advertise our office and to bring new patients, usually flyers include a group of family smiling, but I have seen cartoons also,
The name of the clinic is Belcrest Family dental, address 4382 W Dunlow rd, Katy, TX 77583 , no phone number yet, but you can use any 10 digit number , I don’t have or own any images yet , please the source files of the winner need to have images and the text fields on separate layers to edit if needed promotions, business hours, etc

Target Market(s)

Patient in need of dental work

Industry/Entity Type

Dental Clinic

Font styles to use
Serif
Sans Serif
Script

Colors
34a6d7
0792cd
abd037
9bcb3c
33b8a4

Requirements
Must have
• Images of a family showing their smile
Nice to have
• Design including blue and green colors,
• front and back,
• a section for map location,

```html
<!DOCTYPE html>
<html lang="es">
<head>
<meta charset="utf-8">
<title>Belcrest Family Dental – Flyer</title>
<link href="https://fonts.googleapis.com/css2?family=Fira+Sans:ital,wght@0,400;0,500;0,600;0,700;1,500;1,600;1,700&display=swap" rel="stylesheet">
<style>
  :root{
    --teal:#12a8c9;
    --blue:#0792cd;
    --sky:#34a6d7;
    --light-blue:#8fd3ef;
    --green:#abd037;
    --navy:#1d3f66;
    --ink:#5b6670;
    --strip:#dcf0f7;
    --white:#ffffff;
    --page:#eef2f4;
  }
  *{margin:0;padding:0;box-sizing:border-box;}
  html,body{width:1200px;height:2632px;overflow:hidden;background:var(--page);}
  body{font-family:"Fira Sans",Arial,sans-serif;}
  .flyer{position:absolute;left:0;top:466px;width:1200px;height:1700px;background:var(--white);overflow:hidden;}
  .abs{position:absolute;}

  .brand{left:0;top:70px;width:1200px;display:flex;justify-content:center;align-items:center;gap:22px;}
  .brand-dot{width:70px;height:70px;border-radius:50%;background:var(--teal);}
  .brand-name{font-size:58px;font-weight:500;color:var(--teal);letter-spacing:2px;}

  .headline{left:0;top:212px;width:1200px;text-align:center;font-size:47px;font-weight:700;font-style:italic;color:var(--teal);}
  .intro{left:0;top:292px;width:1200px;text-align:center;font-size:24px;line-height:32px;color:var(--ink);}

  .wave{left:0;top:0;}

  .photo{border-radius:50%;}
  .photo-family{left:61px;top:482px;width:404px;height:404px;border:14px solid var(--white);background:radial-gradient(circle at 45% 40%,#c9a58a,#6f8a5a 70%,#3d5a3a);}
  .photo-kids{left:701px;top:526px;width:264px;height:264px;border:16px solid var(--green);background:radial-gradient(circle at 50% 45%,#9a6a48,#e9ecef 75%);}
  .photo-trio{left:517px;top:763px;width:246px;height:246px;border:14px solid var(--light-blue);background:radial-gradient(circle at 50% 50%,#d6b69d,#f1f3f5 75%);}
  .photo-dentist{left:842px;top:842px;width:358px;height:657px;background:linear-gradient(180deg,#e7c7ad 0%,#f2f4f6 45%,#ffffff 100%);border-radius:180px 0 0 0;}

  .bubble-new{left:318px;top:898px;width:176px;height:176px;border-radius:50%;background:var(--light-blue);color:var(--white);font-size:27px;font-weight:500;line-height:31px;text-align:center;display:flex;align-items:center;justify-content:center;}

  .services-title{left:158px;top:1098px;font-size:31px;font-weight:700;font-style:italic;color:var(--white);}
  .services-mark{left:68px;top:1080px;width:70px;height:70px;border:4px solid var(--white);border-radius:50%;}
  .services-rule{left:158px;top:1145px;width:260px;height:3px;background:var(--white);}
  .services{left:92px;top:1160px;list-style:none;color:var(--white);font-size:22px;font-weight:500;line-height:30.5px;}
  .services li::before{content:"";display:inline-block;width:9px;height:9px;border-radius:50%;background:var(--white);margin-right:12px;vertical-align:middle;}
  .icon{width:58px;height:58px;border-radius:50%;background:var(--white);display:flex;align-items:center;justify-content:center;}
  .icon-1{left:401px;top:1124px;}
  .icon-2{left:401px;top:1254px;}
  .icon-3{left:401px;top:1373px;}

  .member{left:14px;top:1436px;font-size:16px;font-weight:500;color:var(--navy);}

  .heart{left:712px;top:1120px;}
  .heart-text{left:732px;top:1170px;width:152px;text-align:center;font-size:22px;font-weight:500;line-height:25px;color:var(--teal);}

  .map{left:518px;top:1281px;width:210px;height:210px;border-radius:50%;border:6px solid var(--light-blue);background:radial-gradient(circle,#f6f8fa,#e4eaef);}

  .call{left:790px;top:1372px;width:360px;text-align:center;font-size:40px;font-weight:600;color:var(--white);text-shadow:0 0 2px var(--navy),0 0 2px var(--navy);}
  .phone{left:770px;top:1420px;width:400px;text-align:center;font-size:45px;font-weight:700;color:var(--white);text-shadow:0 0 3px var(--navy),0 0 3px var(--navy);}

  .finance{left:0;top:1499px;width:509px;height:141px;background:var(--sky);color:var(--white);text-align:center;}
  .finance-sub{padding-top:26px;font-size:25px;font-weight:600;font-style:italic;}
  .finance-main{font-size:56px;font-weight:700;font-style:italic;line-height:62px;}

  .visit{left:700px;top:1522px;width:500px;text-align:center;font-size:40px;font-weight:500;color:var(--teal);}
  .address{left:700px;top:1584px;width:500px;text-align:center;font-size:25px;font-weight:600;color:var(--navy);}
  .arrow{left:680px;top:1560px;}

  .strip{left:0;top:1640px;width:1200px;height:60px;background:var(--strip);display:flex;justify-content:space-between;align-items:center;padding:0 20px 0 22px;font-size:23px;}
  .strip-left{color:var(--navy);}
  .strip-right{color:var(--navy);font-weight:600;}
</style>
</head>
<body>
<main class="flyer">
  <svg class="abs wave" width="1200" height="1700" viewBox="0 0 1200 1700" aria-hidden="true">
    <path d="M0,472 C180,430 330,400 520,432 C700,462 820,468 960,430 C1060,402 1140,400 1200,420 L1200,1499 L0,1499 Z" fill="var(--teal)"/>
    <path d="M0,520 C250,470 420,455 620,490 C820,525 1000,470 1200,470" fill="none" stroke="var(--white)" stroke-opacity=".35" stroke-width="2" stroke-dasharray="4 6"/>
  </svg>

  <div class="abs brand">
    <span class="brand-dot"></span>
    <span class="brand-name">BELCREST FAMILY DENTAL</span>
  </div>

  <h1 class="abs headline">El amor es más brillante detrás de una sonrisa</h1>
  <p class="abs intro">Estaremos encantados de ayudarle con amabilidad y delicadeza en los tratamientos.<br>Diagnosticamos y aconsejamos el mejor tratamiento para cada caso.<br>Total seguridad, responsabilidad, confianza y honestidad.</p>

  <div class="abs photo photo-family" role="img" aria-label="Foto de una familia sonriendo al aire libre"></div>
  <div class="abs photo photo-kids" role="img" aria-label="Foto de una familia con niños sonriendo"></div>
  <div class="abs photo photo-trio" role="img" aria-label="Foto de padres y niña sonriendo"></div>
  <div class="abs photo-dentist" role="img" aria-label="Foto de una dentista sonriente con bata blanca"></div>

  <div class="abs bubble-new">Nuevo<br>tratamiento<br>odontológico<br>indoloro</div>

  <div class="abs services-mark"></div>
  <h2 class="abs services-title">Nuestros servicios</h2>
  <div class="abs services-rule"></div>
  <ul class="abs services">
    <li>Dentadura postiza</li>
    <li>Extracciones</li>
    <li>Diseño de sonrisa</li>
    <li>Coronas</li>
    <li>Brillo dental</li>
    <li>Tratamiento Alinevo</li>
    <li>Restauración de Implantes</li>
    <li>Parciales</li>
    <li>Blanqueamiento Dental</li>
  </ul>
  <div class="abs icon icon-1"><svg width="30" height="30" viewBox="0 0 30 30"><circle cx="15" cy="10" r="7" fill="var(--teal)"/><path d="M3,29 C4,19 26,19 27,29 Z" fill="var(--teal)"/></svg></div>
  <div class="abs icon icon-2"><svg width="30" height="30" viewBox="0 0 30 30"><path d="M5,6 C8,1 13,4 15,5 C17,4 22,1 25,6 C27,11 23,15 22,22 C21,28 18,28 17,22 C16,18 14,18 13,22 C12,28 9,28 8,22 C7,15 3,11 5,6 Z" fill="var(--teal)"/></svg></div>
  <div class="abs icon icon-3"><svg width="30" height="30" viewBox="0 0 30 30"><rect x="8" y="4" width="3" height="23" rx="1.5" fill="var(--teal)"/><circle cx="9.5" cy="5" r="3.5" fill="var(--teal)"/><rect x="19" y="4" width="3" height="23" rx="1.5" fill="var(--teal)"/></svg></div>

  <p class="abs member">Miembro de la Academia de Odontología General - Dentista General</p>

  <svg class="abs heart" width="190" height="170" viewBox="0 0 190 170" aria-hidden="true">
    <path d="M95,165 C40,125 4,95 4,52 C4,22 28,4 55,4 C74,4 88,14 95,28 C102,14 116,4 135,4 C162,4 186,22 186,52 C186,95 150,125 95,165 Z" fill="var(--white)" stroke="var(--light-blue)" stroke-width="2" stroke-dasharray="4 4"/>
  </svg>
  <p class="abs heart-text">Odontología<br>que hace la<br>Diferencia</p>

  <div class="abs map" role="img" aria-label="Mapa de ubicación de la clínica en 4382 W Dunlow rd"></div>

  <p class="abs call">¡Llamenos hoy!</p>
  <p class="abs phone">1 832-555-0147</p>

  <div class="abs finance">
    <p class="finance-sub">Opciones de Financiamiento</p>
    <p class="finance-main">¡Disponibles!</p>
  </div>

  <svg class="abs arrow" width="70" height="70" viewBox="0 0 70 70" aria-hidden="true">
    <path d="M62,50 C40,54 20,42 10,20" fill="none" stroke="var(--navy)" stroke-width="3"/>
    <path d="M4,28 L10,18 L20,24" fill="none" stroke="var(--navy)" stroke-width="3"/>
  </svg>
  <p class="abs visit">Visitanos en</p>
  <p class="abs address">4382 W Dunlow rd, Katy, TX 77583</p>

  <div class="abs strip">
    <span class="strip-left">La mayoría de los seguros aceptados</span>
    <span class="strip-right">www.BelcrestFamilyDental.com</span>
  </div>
</main>
</body>
</html>
```